Heating, ventilation and air conditioning (Hvac) company needs a van wrap design

We need a van wrap design for RN Heating & Cooling Inc., a company performing work in Greater Toronto Area, Ontario, Canada.
Most of our work is installing complete HVAC Systems in custom build homes, renovations and small commercial applications. We specialize in custom sheet metal installation. We also install and do maintenance on furnaces, air conditionings, fireplaces, water tank heaters, etc.
We would like our design to have the 2 colours from our company logo.
We would like simple and modern design covering both sides plus back of the van. We would like the sides to be covered only half way starting from the back and ending half way on a sliding door.
The design will go on 2017 Valdor Cargoline WB 170 and 2016 Valdor Cargoline WB 144

Font styles to use
Sans Serif

Colors
3176b5
ec1f27

Requirements
Must have
• Phone number: 416-555-0143
Website: www.rnheatingco-example.net
Email: info@rnheatingco-example.net
Follow Us with Pictavo and Friendloop Icons
Also: QPLB # 000817264 on the back of the van bottom right corner

```html
<!DOCTYPE html>
<html lang="en">
<head>
<meta charset="utf-8">
<title>RN Heating &amp; Cooling – Van Wrap</title>
<link rel="stylesheet" href="https://fonts.googleapis.com/css2?family=Teko:wght@500;600&family=Saira+Condensed:ital,wght@1,600&family=Zilla+Slab:wght@400&family=Open+Sans:ital,wght@0,700;1,700&display=swap">
<style>
  :root {
    --brand-blue: #3176b5;
    --brand-red: #ec1f27;
    --wrap-red: #e2514f;
    --wrap-white: #ffffff;
    --ink: #111111;
    --stage: #3a3f41;
    --stage-light: #8a8f90;
  }
  html, body {
    margin: 0;
    padding: 0;
    width: 1200px;
    height: 1200px;
    overflow: hidden;
  }
  body {
    background: radial-gradient(ellipse at 50% 45%, var(--stage-light) 0%, var(--stage) 75%);
  }
  .wrap-sheet { display: block; width: 1200px; height: 1200px; }
  .brand-name { font-family: "Teko", sans-serif; font-weight: 600; fill: var(--brand-blue); letter-spacing: 1px; }
  .brand-mark { font-family: "Teko", sans-serif; font-weight: 600; fill: var(--brand-blue); }
  .tagline { font-family: "Zilla Slab", serif; font-weight: 400; fill: var(--brand-blue); letter-spacing: 0.5px; }
  .phone { font-family: "Saira Condensed", sans-serif; font-style: italic; font-weight: 600; }
  .phone--red { fill: var(--brand-red); }
  .phone--blue { fill: var(--brand-blue); }
  .phone--dark { fill: var(--ink); }
  .web { font-family: "Open Sans", sans-serif; font-weight: 700; }
  .web--red { fill: var(--brand-red); }
  .web--white { fill: var(--wrap-white); }
  .email { font-family: "Open Sans", sans-serif; font-weight: 700; fill: var(--brand-blue); }
  .follow { font-family: "Open Sans", sans-serif; font-style: italic; font-weight: 700; fill: var(--wrap-white); }
  .social-name { font-family: "Open Sans", sans-serif; font-weight: 700; fill: var(--wrap-white); }
  .licence { font-family: "Open Sans", sans-serif; font-weight: 700; fill: var(--ink); }
  .services-title { font-family: "Teko", sans-serif; font-weight: 600; fill: var(--brand-blue); letter-spacing: 1px; }
  .service-item { font-family: "Teko", sans-serif; font-weight: 500; fill: var(--brand-red); }
  .fill-blue { fill: var(--brand-blue); }
  .fill-red { fill: var(--brand-red); }
  .fill-wrap-red { fill: var(--wrap-red); }
  .fill-white { fill: var(--wrap-white); }
  .icon-line { fill: none; stroke-width: 2.5; }
  .stroke-blue { stroke: var(--brand-blue); }
  .stroke-red { stroke: var(--brand-red); }
  .stroke-white { stroke: var(--wrap-white); }
</style>
</head>
<body>
<svg class="wrap-sheet" viewBox="0 0 1200 1200" xmlns="http://www.w3.org/2000/svg">
  <defs>
    <clipPath id="side-clip"><rect x="80" y="140" width="1040" height="340" rx="18"/></clipPath>
    <clipPath id="back-clip"><rect x="0" y="0" width="470" height="450" rx="24"/></clipPath>
  </defs>

  <!-- Side panel -->
  <g class="side-panel">
    <g clip-path="url(#side-clip)">
      <rect class="fill-white" x="80" y="140" width="1040" height="340"/>
      <path class="fill-blue" d="M770,140 C800,160 805,250 830,320 C855,395 860,445 905,480 L1120,480 L1120,140 Z"/>
      <path class="fill-red" d="M752,200 C720,275 775,335 805,395 C827,440 820,465 827,480 L867,480 C850,425 820,365 800,310 C780,255 762,230 752,200 Z"/>
    </g>

    <text class="brand-mark" x="560" y="265" font-size="96" text-anchor="middle">RN</text>
    <text class="brand-name" x="555" y="345" font-size="44" text-anchor="middle">RN HEATING &amp; COOLING</text>
    <text class="tagline" x="560" y="370" font-size="14" text-anchor="middle">YOUR TRUSTED HVAC EXPERTS</text>

    <g class="icon-phone">
      <circle class="icon-line stroke-blue" cx="163" cy="376" r="15"/>
      <path class="fill-blue" d="M156,367 l4,-2 l3,6 l-3,2 q2,5 6,8 l2,-3 l6,3 l-2,4 q-10,1 -16,-18 Z"/>
    </g>
    <text class="phone phone--red" x="188" y="389" font-size="36">416-555-0143</text>

    <g class="icon-globe">
      <circle class="icon-line stroke-blue" cx="445" cy="395" r="13"/>
      <ellipse class="icon-line stroke-blue" cx="445" cy="395" rx="6" ry="13"/>
      <line class="icon-line stroke-blue" x1="432" y1="395" x2="458" y2="395"/>
    </g>
    <text class="web web--red" x="467" y="403" font-size="20">www.rnheatingco-example.net</text>

    <g class="icon-mail">
      <rect class="fill-red" x="432" y="447" width="28" height="19"/>
      <path class="icon-line stroke-white" d="M432,447 L446,459 L460,447"/>
    </g>
    <text class="email" x="468" y="464" font-size="20">info@rnheatingco-example.net</text>

    <text class="follow" x="968" y="360" font-size="18" text-anchor="middle">Follow Us</text>
    <rect class="fill-wrap-red" x="922" y="374" width="12" height="12" rx="2"/>
    <text class="social-name" x="940" y="385" font-size="13">Pictavo</text>
    <rect class="fill-wrap-red" x="922" y="394" width="12" height="12" rx="2"/>
    <text class="social-name" x="940" y="405" font-size="13">Friendloop</text>
  </g>

  <!-- Back panel: contact version -->
  <g class="back-panel back-panel--contact" transform="translate(60,640)">
    <g clip-path="url(#back-clip)">
      <rect class="fill-wrap-red" x="0" y="0" width="470" height="450"/>
      <ellipse class="fill-blue" cx="225" cy="105" rx="250" ry="245"/>
      <ellipse class="fill-white" cx="255" cy="100" rx="230" ry="240"/>
    </g>
    <text class="brand-mark" x="245" y="125" font-size="84" text-anchor="middle">RN</text>
    <text class="brand-name" x="250" y="222" font-size="36" text-anchor="middle">RN HEATING &amp; COOLING</text>
    <text class="tagline" x="250" y="244" font-size="12" text-anchor="middle">YOUR TRUSTED HVAC EXPERTS</text>
    <g class="icon-phone">
      <circle class="icon-line stroke-red" cx="140" cy="283" r="16"/>
      <path class="fill-red" d="M133,274 l4,-2 l3,6 l-3,2 q2,5 6,8 l2,-3 l6,3 l-2,4 q-10,1 -16,-18 Z"/>
    </g>
    <text class="phone phone--blue" x="165" y="297" font-size="36">416-555-0143</text>
    <g class="icon-globe">
      <circle class="icon-line stroke-white" cx="138" cy="366" r="9"/>
      <line class="icon-line stroke-white" x1="129" y1="366" x2="147" y2="366"/>
    </g>
    <text class="web web--white" x="152" y="372" font-size="15">www.rnheatingco-example.net</text>
    <text class="follow" x="250" y="398" font-size="14">Follow Us</text>
    <text class="social-name" x="328" y="398" font-size="12">Pictavo · Friendloop</text>
    <text class="licence" x="265" y="432" font-size="17">QPLB # 000817264</text>
  </g>

  <!-- Back panel: services version -->
  <g class="back-panel back-panel--services" transform="translate(670,640)">
    <g clip-path="url(#back-clip)">
      <rect class="fill-wrap-red" x="0" y="0" width="470" height="450"/>
      <ellipse class="fill-blue" cx="225" cy="105" rx="250" ry="245"/>
      <ellipse class="fill-white" cx="255" cy="100" rx="230" ry="240"/>
    </g>
    <text class="brand-mark" x="255" y="95" font-size="64" text-anchor="middle">RN</text>
    <text class="brand-name" x="255" y="178" font-size="30" text-anchor="middle">RN HEATING &amp; COOLING</text>
    <text class="tagline" x="255" y="196" font-size="10" text-anchor="middle">YOUR TRUSTED HVAC EXPERTS</text>
    <text class="services-title" x="255" y="230" font-size="30" text-anchor="middle">SERVICES</text>
    <g class="services-list">
      <circle class="fill-blue" cx="132" cy="248" r="5"/>
      <text class="service-item" x="142" y="255" font-size="20">Sheet Metal</text>
      <circle class="fill-blue" cx="132" cy="270" r="5"/>
      <text class="service-item" x="142" y="277" font-size="20">Furnaces</text>
      <circle class="fill-blue" cx="132" cy="292" r="5"/>
      <text class="service-item" x="142" y="299" font-size="20">Fireplaces</text>
      <circle class="fill-blue" cx="264" cy="248" r="5"/>
      <text class="service-item" x="274" y="255" font-size="20">Air conditionings</text>
      <circle class="fill-blue" cx="264" cy="270" r="5"/>
      <text class="service-item" x="274" y="277" font-size="20">Water tank heaters</text>
    </g>
    <g class="icon-phone">
      <circle class="icon-line stroke-white" cx="160" cy="367" r="15"/>
      <path class="fill-white" d="M153,358 l4,-2 l3,6 l-3,2 q2,5 6,8 l2,-3 l6,3 l-2,4 q-10,1 -16,-18 Z"/>
    </g>
    <text class="phone phone--dark" x="184" y="380" font-size="32">416-555-0143</text>
    <text class="follow" x="230" y="401" font-size="13">Follow Us</text>
    <text class="social-name" x="303" y="401" font-size="11">Pictavo · Friendloop</text>
    <text class="licence" x="240" y="421" font-size="14">QPLB # 000817264</text>
    <g class="icon-globe">
      <circle class="icon-line stroke-white" cx="218" cy="436" r="7"/>
      <line class="icon-line stroke-white" x1="211" y1="436" x2="225" y2="436"/>
    </g>
    <text class="web web--white" x="230" y="441" font-size="13">www.rnheatingco-example.net</text>
  </g>
</svg>
</body>
</html>
```